Personal contact Business card design needed

I work in the Property Industry - specifically Property Management.

I need a card I can hand out to colleagues at networking events, meetings, training courses etc. that will provide my contact details.

Target Market(s)

Professional colleagues / potential clients / employers

Industry/Entity Type

Training

Contact Information for Business Card

I need a simple and professional card to give to professional network contacts at meetings, interviews etc.

The card should include my photograph, name, mobile number, email address and Proflinx address.

I would like appropriate professional colours. Something feminine but not too 'frilly' or 'girly'

Requirements
Must have
• Photograph of myself.
I want it to be simple,perhaps a small icon for each contact detail such as
Email icon
Proflinx icon
Mobile number

```html
<!DOCTYPE html>
<html lang="en">
<head>
<meta charset="utf-8">
<title>Karen Doyle – Business Card</title>
<link href="https://fonts.googleapis.com/css2?family=Montserrat:wght@400;500;700&display=swap" rel="stylesheet">
<style>
  :root {
    --page-bg: #2b2b2d;
    --card-light: #e6e8ea;
    --card-mid: #c9ccd0;
    --card-dark: #aeb2b7;
    --ink: #1c1c1e;
    --ink-soft: #2e2f31;
    --photo-top: #5a3a2e;
    --photo-mid: #3a2520;
    --photo-base: #1d1b1d;
  }
  * { box-sizing: border-box; margin: 0; padding: 0; }
  html, body {
    width: 1200px;
    height: 860px;
    overflow: hidden;
    background: var(--page-bg);
  }
  .card {
    position: absolute;
    left: 100px;
    top: 144px;
    width: 1000px;
    height: 572px;
    background: radial-gradient(ellipse at 70% 30%, var(--card-light) 0%, var(--card-mid) 55%, var(--card-dark) 100%);
    overflow: hidden;
    font-family: "Montserrat", Arial, sans-serif;
    color: var(--ink);
  }
  .portrait {
    position: absolute;
    left: 90px;
    top: 150px;
    width: 380px;
    height: 422px;
    border-radius: 170px 170px 0 0;
    background: linear-gradient(180deg, var(--photo-top) 0%, var(--photo-mid) 45%, var(--photo-base) 100%);
  }
  .identity {
    position: absolute;
    left: 480px;
    top: 150px;
  }
  .name {
    font-size: 44px;
    font-weight: 700;
    letter-spacing: 0.5px;
    line-height: 1.1;
  }
  .role {
    font-size: 25px;
    font-weight: 400;
    color: var(--ink-soft);
    margin-top: 4px;
  }
  .contacts {
    list-style: none;
    margin-top: 34px;
    font-size: 23px;
    color: var(--ink-soft);
  }
  .contacts li {
    display: flex;
    align-items: center;
    gap: 20px;
    height: 36px;
  }
  .contacts svg {
    width: 24px;
    height: 24px;
    flex: none;
    fill: var(--ink);
  }
</style>
</head>
<body>
  <main class="card">
    <div class="portrait" role="img" aria-label="Portrait photograph of Karen Doyle"></div>
    <section class="identity">
      <h1 class="name">Karen Doyle</h1>
      <p class="role">Property Management Specialist</p>
      <ul class="contacts">
        <li>
          <svg viewBox="0 0 24 24" aria-hidden="true"><path d="M3 9c0-3 4-5 9-5s9 2 9 5v2h-5V9c-1-1-7-1-8 0v2H3z"/><path d="M6 13h12l2 7H4z"/></svg>
          <span>0400 555 123</span>
        </li>
        <li>
          <svg viewBox="0 0 24 24" aria-hidden="true"><path d="M2 5h20v14H2z"/><path d="M2 5l10 8 10-8" fill="none" stroke="#d5d8dc" stroke-width="1.6"/></svg>
          <span>karen@mailbox.com.au</span>
        </li>
        <li>
          <svg viewBox="0 0 24 24" aria-hidden="true"><rect x="4" y="4" width="16" height="16"/></svg>
          <span>au.proflinx.com/in/karendoyleaus</span>
        </li>
      </ul>
    </section>
  </main>
</body>
</html>
```